Real Estate "For Sale" Sign for construction company

We need a sign that we can use to hang on a post and place on the road when we sell a property. The sign will be simple and will need to mainly feature our logo (files attached), as well as the words "For Sale", and then our phone number "(555) 617 3489". The sign will hang on a post that'll look something like the attached picture.

Target Market(s)

Home buyers

Industry/Entity Type

Real Estate

Font styles to use
Serif
Sans Serif

Colors
0054AA
0677BA
7BADD7
CADEEF
E8F1F8
0094D4
00A9DD
6FCCEA
C7EBF8
E9F6FB

Requirements
Must have
• For Sale & our phone number

```html
<!DOCTYPE html>
<html lang="en">
<head>
<meta charset="utf-8">
<title>For Sale Sign</title>
<link rel="stylesheet" href="https://fonts.googleapis.com/css2?family=Roboto+Condensed:wght@700&family=Roboto:wght@400;700&display=swap">
<style>
  :root {
    --sky: #8fd7f7;
    --navy: #19204c;
    --white: #ffffff;
  }
  html, body {
    margin: 0;
    padding: 0;
    overflow: hidden;
    background: var(--sky);
  }
  .sign {
    display: block;
    width: 960px;
    height: 1200px;
  }
  .sign__top { fill: var(--sky); }
  .sign__bottom { fill: var(--navy); }
  .sign__rule { stroke: var(--navy); stroke-width: 2; }
  .brand-name {
    font-family: "Roboto Condensed", "Arial Narrow", sans-serif;
    font-weight: 700;
    font-size: 58px;
    fill: var(--navy);
    letter-spacing: 1px;
  }
  .headline {
    font-family: "Roboto Condensed", "Arial Narrow", sans-serif;
    font-weight: 700;
    font-size: 264px;
    fill: var(--white);
  }
  .contact-label {
    font-family: "Roboto", Arial, sans-serif;
    font-weight: 400;
    font-size: 69px;
    fill: var(--white);
  }
  .contact-phone {
    font-family: "Roboto", Arial, sans-serif;
    font-weight: 700;
    font-size: 137px;
    fill: var(--white);
  }
</style>
</head>
<body>
<svg class="sign" width="960" height="1200" viewBox="0 0 960 1200" xmlns="http://www.w3.org/2000/svg">
  <rect class="sign__top" x="0" y="0" width="960" height="815"/>
  <rect class="sign__bottom" x="0" y="815" width="960" height="385"/>

  <g class="brand">
    <text class="brand-name" x="480" y="248" text-anchor="middle">HIGHLAND OAK HOMES</text>
  </g>

  <line class="sign__rule" x1="24" y1="457" x2="935" y2="457"/>

  <text class="headline" x="63" y="723" textLength="841" lengthAdjust="spacingAndGlyphs">FOR SALE</text>

  <text class="contact-label" x="248" y="942" textLength="464" lengthAdjust="spacingAndGlyphs">CALL OR TEXT:</text>
  <text class="contact-phone" x="60" y="1092" textLength="843" lengthAdjust="spacingAndGlyphs">(555) 617 3489</text>
</svg>
</body>
</html>
```